Boutique custom software development company needs new business card

Our nearly 20 year old custom software development company would like to better include the fact that we are now providing Bitcoin services. These new services are B2B include education (how to acquire and securely hold Bitcoin) and integrating Bitcoin payments into existing ecommerce sites or other existing systems. Please keep the card clean and simple. Attached is our current design and some other files. vexalon.example

Target Market(s)

businesses owners interested in long term relationship

Industry/Entity Type

Custom software development and Bitcoin

Contact Information for Business Card

Marcus Ellwood, marcus@vexalon.example, vexalon.example, (888) 555-VEXAL

Font styles to use
Other font styles liked:
• monospace

Requirements
Must have
• double-sided
Nice to have
• clean and simple
Should not have
• physical address

```html
<!DOCTYPE html>
<html lang="en">
<head>
<meta charset="utf-8">
<title>Vexalon Business Card</title>
<link rel="stylesheet" href="https://fonts.googleapis.com/css2?family=Archivo+Black&family=Open+Sans:wght@300;400;700&family=Arimo:wght@400&display=swap">
<style>
  :root {
    --blue: #3a6aad;
    --orange: #e87722;
    --paper: #f7f7f5;
    --ink: #1e1e1e;
    --backdrop: #3a3230;
  }
  * { margin: 0; padding: 0; box-sizing: border-box; }
  html, body { width: 1200px; height: 912px; overflow: hidden; }
  body {
    background: var(--backdrop);
    position: relative;
    font-family: "Open Sans", sans-serif;
  }
  .card {
    position: absolute;
    width: 600px;
    height: 343px;
    background: var(--paper);
    overflow: hidden;
    box-shadow: 0 6px 18px rgba(0,0,0,.35);
  }
  .card--front { left: 300px; top: 70px; }
  .card--back { left: 300px; top: 498px; }

  /* Front */
  .brand {
    position: absolute;
    left: 118px;
    top: 96px;
    display: flex;
    align-items: center;
    gap: 12px;
  }
  .brand__mark {
    width: 34px;
    height: 34px;
    background: var(--orange);
  }
  .brand__name {
    font-weight: 700;
    font-size: 58px;
    line-height: 1;
    color: var(--blue);
    letter-spacing: 1px;
  }
  .tagline {
    position: absolute;
    left: 120px;
    top: 166px;
    font-weight: 300;
    font-size: 25px;
    color: var(--blue);
    letter-spacing: -0.5px;
  }
  .front-url {
    position: absolute;
    right: 70px;
    bottom: 60px;
    font-family: "Archivo Black", sans-serif;
    font-size: 15px;
    letter-spacing: 1.5px;
    color: var(--blue);
  }
  .front-url span { color: var(--orange); }

  /* Back */
  .back-art {
    position: absolute;
    left: 0;
    top: 0;
    width: 220px;
    height: 343px;
  }
  .person {
    position: absolute;
    right: 40px;
    top: 48px;
    text-align: right;
  }
  .person__name {
    font-family: "Archivo Black", sans-serif;
    font-size: 31px;
    color: var(--blue);
    line-height: 1.05;
  }
  .person__role {
    font-family: "Arimo", sans-serif;
    font-size: 17px;
    color: var(--orange);
    margin-top: 2px;
  }
  .contact {
    position: absolute;
    right: 40px;
    top: 198px;
    list-style: none;
    font-family: "Arimo", sans-serif;
    font-size: 17px;
    color: var(--ink);
    text-align: right;
  }
  .contact li {
    display: flex;
    align-items: center;
    justify-content: flex-end;
    gap: 8px;
    line-height: 24px;
  }
  .contact svg { width: 14px; height: 14px; flex: none; }
</style>
</head>
<body>

<section class="card card--front" aria-label="Card front">
  <div class="brand">
    <span class="brand__mark"></span>
    <span class="brand__name">VEXALON</span>
  </div>
  <p class="tagline">developer of custom applications</p>
  <p class="front-url">www.<span>vexalon</span>.example</p>
</section>

<section class="card card--back" aria-label="Card back">
  <svg class="back-art" viewBox="0 0 220 343" aria-hidden="true">
    <rect x="0" y="0" width="150" height="343" fill="var(--blue)"/>
    <rect x="0" y="258" width="150" height="85" fill="var(--orange)"/>
  </svg>

  <div class="person">
    <h1 class="person__name">Marcus Ellwood</h1>
    <p class="person__role">Bitcoin educator</p>
  </div>

  <ul class="contact">
    <li>(888) 555-VEXAL
      <svg viewBox="0 0 16 16" aria-hidden="true"><path fill="var(--orange)" d="M3.6 1.2l2.3 2.6-1.2 1.8c.9 2 2.6 3.7 4.7 4.7l1.8-1.2 2.6 2.3-1.3 2.3C7 13.4 2.6 9 1.3 2.5z"/></svg>
    </li>
    <li>marcus@vexalon.example
      <svg viewBox="0 0 16 16" aria-hidden="true"><rect x="1" y="3" width="14" height="10" fill="var(--orange)"/><path d="M1.5 3.5L8 9l6.5-5.5" fill="none" stroke="var(--paper)" stroke-width="1.3"/></svg>
    </li>
    <li>www.vexalon.example
      <svg viewBox="0 0 16 16" aria-hidden="true"><circle cx="8" cy="8" r="7" fill="var(--orange)"/><path d="M1 8h14M8 1c-3 3.5-3 10.5 0 14M8 1c3 3.5 3 10.5 0 14" fill="none" stroke="var(--paper)" stroke-width="1"/></svg>
    </li>
  </ul>
</section>

</body>
</html>
```